Travinex - You are the Boss!

Travinex is a new Silicon Valley company, of the pelim founders from Berlin, which provides a "Shared Pioneer Circle". This platform allows the crowd to support startups with money, experts and fame. Our Vision is, that everyone should become an entrepreneur.

Pls find all brief details in the attached document
Updates

Would be nice to have a list of more social services I'm available on, like a list of pictograms of all my services:

Find me on: vooka, bramlet+, qrt, fenwix, moodrail, zupp, hvoxa, etc...

pls make sure to use the right font:
http://www.typemarlow.com/fonts/Velquin

Target Market(s)

Main target market is those already involved in the startup industry, by fundraising, investing, advising, cofounding and working. Travinex brings a totaly new transparency and collaborative way of starting companies to that business.

· Entrepreneurs (looking for funding, team and community)
· Investors (looking for hot investments and )
· Experts (workers looking for startups they can work for equity)
· Incubators & Business Schools (looking for tools to advise startups)

Industry/Entity Type

It Company

Requirements
Must have
• Pls find all brief details in the attached document
Nice to have

```html
<!DOCTYPE html>
<html lang="en">
<head>
<meta charset="utf-8">
<title>Travinex – Business Card</title>
<link rel="stylesheet" href="https://fonts.googleapis.com/css2?family=Open+Sans:wght@400;600;700&display=swap">
<style>
  :root {
    --card-dark: #2b2b2b;
    --brand-orange: #f26a3a;
    --brand-orange-deep: #ef6532;
    --ink-light: #ffffff;
    --ink-muted: #e6e6e6;
    --stage-light: #f4f4f4;
    --stage-mid: #c9c9cb;
    --stage-dark: #b6b6b8;
  }
  * { margin: 0; padding: 0; box-sizing: border-box; }
  html, body {
    width: 1121px;
    height: 1200px;
    overflow: hidden;
  }
  body {
    position: relative;
    font-family: "Open Sans", "Segoe UI", sans-serif;
    background: linear-gradient(100deg, var(--stage-dark) 0%, var(--stage-mid) 22%, var(--stage-light) 48%, var(--stage-mid) 75%, var(--stage-dark) 100%);
  }
  .card {
    position: absolute;
    left: 225px;
    width: 654px;
    height: 378px;
    overflow: hidden;
    color: var(--ink-light);
  }
  /* Front */
  .card--front {
    top: 196px;
    background: var(--card-dark);
  }
  .card--front .accent-band {
    position: absolute;
    left: 0; right: 0; bottom: 0;
    height: 25px;
    background: var(--brand-orange);
  }
  .holder {
    position: absolute;
    left: 36px;
    top: 66px;
    text-align: right;
  }
  .holder__name {
    font-size: 32px;
    font-weight: 700;
    line-height: 1;
    letter-spacing: 0.2px;
  }
  .holder__role {
    margin-top: 14px;
    font-size: 18px;
    font-weight: 400;
    color: var(--ink-muted);
  }
  .brand {
    position: absolute;
    right: 34px;
    top: 34px;
    display: flex;
    flex-direction: column;
    align-items: center;
  }
  .brand__mark {
    display: flex;
    align-items: center;
    gap: 8px;
    font-size: 28px;
    font-weight: 700;
    color: var(--brand-orange);
    line-height: 1;
  }
  .brand__dot {
    width: 18px;
    height: 18px;
    border-radius: 50%;
    background: var(--brand-orange);
  }
  .brand__tagline {
    margin-top: 10px;
    font-size: 16px;
    font-weight: 700;
  }
  .contacts {
    position: absolute;
    right: 28px;
    top: 240px;
    list-style: none;
    text-align: right;
    font-size: 19px;
    line-height: 24px;
    color: var(--ink-muted);
  }
  /* Back */
  .card--back {
    top: 616px;
    background: var(--brand-orange-deep);
  }
  .brand-watermark {
    position: absolute;
    left: 0; right: 0;
    top: 60px;
    text-align: center;
    font-size: 140px;
    font-weight: 700;
    color: rgba(255, 255, 255, 0.08);
    line-height: 1;
  }
  .pitch {
    position: absolute;
    left: 0; right: 0;
    top: 196px;
    list-style: none;
    text-align: center;
    font-size: 23px;
    line-height: 31px;
  }
</style>
</head>
<body>
  <section class="card card--front" aria-label="Card front">
    <div class="holder">
      <h1 class="holder__name">Marten Kessow</h1>
      <p class="holder__role">Founder and CEO</p>
    </div>
    <div class="brand">
      <div class="brand__mark"><span class="brand__dot"></span>Travinex</div>
      <p class="brand__tagline">You are the Boss!</p>
    </div>
    <ul class="contacts">
      <li>the@travinex.com</li>
      <li>chirpline.com/martenkessow</li>
      <li>facelink.com/martenkessow</li>
      <li>workgrid.com/in/martenkessow</li>
    </ul>
    <div class="accent-band"></div>
  </section>

  <section class="card card--back" aria-label="Card back">
    <div class="brand-watermark" aria-hidden="true">Travinex</div>
    <ul class="pitch">
      <li>Are you interested in?</li>
      <li>Starting your own Business?</li>
      <li>Investing in hot Startups?</li>
      <li>Working for the next “Facelink”?</li>
      <li>Join us on Facelink.com/Travinex</li>
    </ul>
  </section>
</body>
</html>
```